Quenderix (www.quenderix-demo.net) needs exciting professional PowerPoint pitch template

Quenderix is an exciting new start-up targeting innovative ways to engage with retail customers at the point of sale.

Our customers are looking for us to help them increase the "wallet share" of their retail customers. The retail customer has their wallet open at the Point of Sale and are paying money to our customer. At Quenderix we are all about attracting the attention of the retail customer AT THAT POINT IN TIME and engaging the retail customer in spending a little more in that store or another store that has a relationship to the retail customer's purchase.

Our customers are the owners of very large supermarkets, chain stores, and financial institutions, and therefore when we pitch a proposal to these buyers it needs to be slick, professional, and very memorable.

The PowerPoint sales presentation template is a key part of striking that impression.

Here is some background...

Our Vision
Through applying new thinking to a mature industry we are reinventing selected segments of the Australian retail messaging business, generating significant value for our customers, our suppliers, and our owners.
We operate with integrity, agility, and intelligence to doing things smarter, faster and more efficiently.
We bring deep industry expertise, deep relationships with customers and suppliers, and a will to see the old ways give way to smarter ways – this is why we win.
From this economically sustainable platform, we will examine the disruption of other market segments by further leveraging the elements that make us successful.

Our Values
With our clients, with our suppliers, with our staff, and with our owners:
# We Partner – We align the interest of all stakeholders by striving to ensure everything we do is mutually beneficial and commercially sustainable in the long term. We are clear with all our stakeholders about what our expectations are of them, and we seek clarity from them in their expectations of us.
# We Innovate – In the segments we choose to compete in, we bring fresh ideas, new business processes, the right relationships, and the right technology to ensure the supply chain is nimble, competitive, and reliable.
# We are Accountable – We say what we will do, and then do what we say.
# We Perform – We use our skills, relationships, and reputation to deliver value to our customers, suppliers, and owners.

Initially we are building our business from low-tech through printing promotional offers and retailer messages on ATM and EFTPOS receipts, but as soon as cash flow supports it we will be engaging in high-tech real-time targeted offers to the specific consumer through video wall offers as people are at the checkout or walking through the shopping centre.

I'd like the PowerPoint template to reflect our vision and values.

The PowerPoint template will be used in communicating our proposals to our clients, and needs to catch and hold our audiences attention.

Please check out the web site we have just launched - it is pretty basic but it has only been up a week. We intend to sharpen it over the coming weeks, but you'll get the idea of what our core messages are.

I have recently sourced a logo from Sketchloft, plus business cards, and have attached the source files for your reference.
Updates

Hi everybody.  Thanks for the designs submitted so far.  Your submissions have helped me understand what I do and don't prefer, and I have updated the "Must Have/Nice to Have/Shouldn't Have" criteria accordingly.  I have also uploaded a powerpoint template that I had at a company I udsed to run that has the sort of visual theme I find appealing. I have more time to provide feedback now that the week is over, so I will comment on individual designs shortly, and I will respond to queries directed to me.

Kind Regards - Gareth

Target Market(s)

Our customers are large corporations that have professional Point Of Sale marketing experts looking for a supplier with an edge over others in a crowded market. The buyer of our product and services is ultimately a communications expert. They want to see distinctive competence, and an agility of thinking that will make them money through driving more consumer spending.

Industry/Entity Type

Financial

Font styles to use
Sans Serif

Colors
34a7d7
0892cd
3276b5

Requirements
Must have
• The following Slides: Title Slide, Agenda, About Quenderix, Thank you
The pages must be easy on the eye.
The final product must be a PowerPoint template file with the usual "Title", "Title and Content", "Title & Table", and "Blank" page types.
Widescreen format please.
Nice to have
• The pages should have an eye-catching visual element running through all the pages. I have attached a template from a company i used to be involved with that has a visual theme running through it that I like.
Plenty of whitespace - have a look at www.quenderix-demo.net.
Bonus points for pulling the text from the brief into the template.
Use "Innovation - Integrity - Service" as the tag line.
Should not have
• Pages should not be busy.
Stay away from too much black. I know the cards have black, but the presentation shouldn't.
I dont like serifed fonts. Use Blenvotz's Fjord Kit style for insporation.
The "Keeping Vivid" tag line was an invention of the logo designer that we do not want to cary forward. Please do not use it.

```html
<!DOCTYPE html>
<html lang="en">
<head>
<meta charset="utf-8">
<title>Quenderix Presentation Template</title>
<link rel="stylesheet" href="https://fonts.googleapis.com/css2?family=Arimo:ital,wght@0,400;0,500;0,700;1,400&display=swap">
<style>
:root{
  --board:#a1a1a1;
  --slide:#ffffff;
  --frame:#d4d4d4;
  --brand:#2b6db3;
  --brand-light:#34a7d7;
  --ink:#222222;
  --muted:#8a8a8a;
  --faint:#c4c4c4;
  --bar-1:#0d78c2;
  --bar-2:#2d6aa0;
  --bar-3:#f99a0a;
  --bar-4:#97ac2c;
  --bar-5:#f26a0f;
  --row-a:#dedede;
  --row-b:#f1f1f1;
}
*{box-sizing:border-box;margin:0;padding:0}
html,body{width:1200px;height:900px;overflow:hidden;background:var(--board);font-family:"Arimo",Arial,sans-serif;color:var(--ink)}
.board{position:relative;width:1200px;height:900px}
.slide{position:absolute;width:325px;height:243px;background:var(--slide);overflow:hidden}
.slide--framed{border:3px solid var(--frame)}
.s-title{left:60px;top:40px}
.s-divider{left:418px;top:40px;border:3px solid var(--frame)}
.s-about{left:771px;top:40px}
.s-agenda{left:60px;top:311px}
.s-only{left:418px;top:311px}
.s-bullets{left:771px;top:311px}
.s-table{left:60px;top:592px}
.s-thanks{left:417px;top:592px}
.slide-title{position:absolute;left:16px;top:14px;font-size:13px;font-weight:400;color:var(--ink)}
.brand{color:var(--brand);font-weight:500;white-space:nowrap}
.brand--large{font-size:19px}
.brand--small{position:absolute;right:12px;bottom:6px;font-size:8px}
.cover-photo{position:absolute;left:48px;top:6px;width:232px;height:108px;border-radius:6px;background:linear-gradient(90deg,#6a5a3a 0%,#d9d9d6 35%,#d9d9d6 62%,#9a7656 100%)}
.cover-brand{position:absolute;left:0;right:0;top:126px;text-align:center}
.cover-heading{position:absolute;left:0;right:0;top:184px;text-align:center;font-size:11px;font-weight:500;color:var(--brand)}
.cover-date{position:absolute;left:0;right:0;top:202px;text-align:center;font-size:6px;color:var(--faint)}
.divider-photo{position:absolute;inset:0;background:linear-gradient(100deg,#dcdcd8 0%,#cfcfca 38%,#8a8a86 52%,#d6d6d0 70%,#2a2a2a 100%)}
.divider-brand{position:absolute;left:15px;top:40px}
.divider-label{position:absolute;left:15px;top:170px;font-size:9px;color:var(--brand)}
.about-lead{position:absolute;left:40px;right:40px;top:38px;text-align:center;font-size:5.3px;line-height:1.4;color:var(--brand)}
.about-cols{position:absolute;left:20px;right:20px;top:60px;display:flex;justify-content:space-between}
.about-col{width:72px}
.about-col h3{font-size:4.6px;font-weight:400;color:var(--brand);text-align:center;margin-bottom:3px}
.about-photo{height:40px;border:1px solid #999}
.about-col p{font-size:3.6px;line-height:1.35;color:#444;margin-top:3px}
.about-col em{font-style:normal;color:var(--brand-light)}
.agenda-row{position:absolute;left:16px;width:288px;height:26px}
.agenda-label{position:absolute;left:0;top:8px;font-size:6px;font-style:italic;color:var(--muted)}
.agenda-arrow{position:absolute;left:36px;top:9px}
.agenda-bar{position:absolute;left:56px;right:0;top:0;height:26px;border-radius:3px;color:#fff;padding:3px 6px}
.agenda-title{display:block;font-size:6px;font-weight:400}
.agenda-sub{display:block;font-size:4.5px;margin-top:2px}
.bullets-title{top:31px;font-size:12px}
.bullets{position:absolute;left:0;top:48px;font-size:7.4px;line-height:11.3px;color:var(--ink);list-style:none}
.bullets li{position:relative;color:var(--ink)}
.bullets li::before{position:absolute}
.l1{padding-left:24px}.l1::before{content:"•";left:17px}
.l2{padding-left:40px}.l2::before{content:"–";left:33px}
.l3{padding-left:56px}.l3::before{content:"•";left:50px}
.l4{padding-left:72px}.l4::before{content:"–";left:65px}
.l5{padding-left:87px}.l5::before{content:"•";left:81px}
.data-table{position:absolute;left:15px;top:55px;width:293px;border-collapse:collapse;font-size:4.8px}
.data-table th{background:var(--bar-1);color:#fff;font-weight:400;height:14px;text-align:center;border-right:1px solid #fff}
.data-table th:first-child{text-align:left;padding-left:4px}
.data-table td{height:14px;text-align:center;color:#444}
.data-table td:first-child{text-align:left;padding-left:4px}
.data-table tr:nth-child(odd) td{background:var(--row-a)}
.data-table tr:nth-child(even) td{background:var(--row-b)}
</style>
</head>
<body>
<main class="board">

  <section class="slide slide--framed s-title">
    <div class="cover-photo" role="img" aria-label="Photo collage of coins, stacked receipt paper rolls and a warehouse"></div>
    <div class="cover-brand brand brand--large">Quenderix</div>
    <h1 class="cover-heading">Presentation Heading</h1>
    <p class="cover-date">November 15, 2013</p>
  </section>

  <section class="slide s-divider">
    <div class="divider-photo" role="img" aria-label="Photograph of receipt paper rolls stacked on a dark background"></div>
    <div class="divider-brand brand brand--large">Quenderix</div>
    <p class="divider-label">DIVIDER</p>
  </section>

  <section class="slide slide--framed s-about">
    <h2 class="slide-title">About Us</h2>
    <p class="about-lead">Quenderix is bringing new thinking to a mature industry, reinventing selected segments of the Australian POS messaging business, generating game changing value for our customers</p>
    <div class="about-cols">
      <article class="about-col">
        <h3>Outcomes over Products...</h3>
        <div class="about-photo" style="background:linear-gradient(#e6e6e3,#bdbdb8)" role="img" aria-label="Photograph of two paper rolls"></div>
        <p>At Quenderix, understanding your goals and your business drives everything we do. Coupled with deep expertise in retail messaging, we help you reach the customer while their wallet is open, turning each receipt into a real chance to lift spend and build lasting loyalty across your stores.</p>
      </article>
      <article class="about-col">
        <h3>The Quenderix difference...</h3>
        <div class="about-photo" style="background:linear-gradient(#7d6a58,#b07a4a)" role="img" aria-label="Photograph of a warehouse interior"></div>
        <p>We have redefined best practice in the Australian printing and messaging industry. <em>Innovation:</em> we never fail to learn and share new ideas. <em>Integrity:</em> we say what we will do, and then do what we say. <em>Service:</em> we stay close to every partner and keep them informed every single day.</p>
      </article>
      <article class="about-col">
        <h3>How we serve you...</h3>
        <div class="about-photo" style="background:linear-gradient(#2b3346,#5a5a52)" role="img" aria-label="Photograph of an office building at night"></div>
        <p><em>Focus:</em> we serve a small number of large retail and financial partners. We understand the complexity of your distribution channel and your need for timely delivery of quality product. Account management, production and dispatch are built around you to ensure your confidence stays high.</p>
      </article>
    </div>
    <div class="brand brand--small">Quenderix</div>
  </section>

  <section class="slide slide--framed s-agenda">
    <h2 class="slide-title">Agenda</h2>
    <div class="agenda-row" style="top:50px"><span class="agenda-label">Text 5</span><svg class="agenda-arrow" width="8" height="7" viewBox="0 0 8 7"><path d="M0 2.5h4V0l4 3.5L4 7V4.5H0z" fill="var(--muted)"/></svg><div class="agenda-bar" style="background:var(--bar-5)"><span class="agenda-title">Title</span><span class="agenda-sub">Subtitle</span></div></div>
    <div class="agenda-row" style="top:85px"><span class="agenda-label">Text 4</span><svg class="agenda-arrow" width="8" height="7" viewBox="0 0 8 7"><path d="M0 2.5h4V0l4 3.5L4 7V4.5H0z" fill="var(--muted)"/></svg><div class="agenda-bar" style="background:var(--bar-4)"><span class="agenda-title">Title</span><span class="agenda-sub">Subtitle</span></div></div>
    <div class="agenda-row" style="top:119px"><span class="agenda-label">Text 3</span><svg class="agenda-arrow" width="8" height="7" viewBox="0 0 8 7"><path d="M0 2.5h4V0l4 3.5L4 7V4.5H0z" fill="var(--muted)"/></svg><div class="agenda-bar" style="background:var(--bar-3)"><span class="agenda-title">Title</span><span class="agenda-sub">Subtitle</span></div></div>
    <div class="agenda-row" style="top:153px"><span class="agenda-label">Text 2</span><svg class="agenda-arrow" width="8" height="7" viewBox="0 0 8 7"><path d="M0 2.5h4V0l4 3.5L4 7V4.5H0z" fill="var(--muted)"/></svg><div class="agenda-bar" style="background:var(--bar-2)"><span class="agenda-title">Title</span><span class="agenda-sub">Subtitle</span></div></div>
    <div class="agenda-row" style="top:188px"><span class="agenda-label">Text 1</span><svg class="agenda-arrow" width="8" height="7" viewBox="0 0 8 7"><path d="M0 2.5h4V0l4 3.5L4 7V4.5H0z" fill="var(--muted)"/></svg><div class="agenda-bar" style="background:var(--bar-1)"><span class="agenda-title">Title</span><span class="agenda-sub">Subtitle</span></div></div>
    <div class="brand brand--small">Quenderix</div>
  </section>

  <section class="slide slide--framed s-only">
    <h2 class="slide-title" style="top:24px">Title Only</h2>
    <div class="brand brand--small">Quenderix</div>
  </section>

  <section class="slide slide--framed s-bullets">
    <h2 class="slide-title bullets-title">Title and Bulleted Content</h2>
    <ul class="bullets">
      <li class="l1">Click to edit Master text styles</li>
      <li class="l2">Second level</li>
      <li class="l3">Third level</li>
      <li class="l4">Fourth level</li>
      <li class="l5">Fifth level</li>
    </ul>
    <div class="brand brand--small">Quenderix</div>
  </section>

  <section class="slide slide--framed s-table">
    <h2 class="slide-title" style="top:24px">Table</h2>
    <table class="data-table">
      <thead><tr><th>Title A</th><th>Title B</th><th>Title C</th><th>Title D</th><th>Title E</th></tr></thead>
      <tbody>
        <tr><td>Text here</td><td>1234567890</td><td>1234567890</td><td>1234567890</td><td>1234567890</td></tr>
        <tr><td>Text here</td><td>1234567890</td><td>1234567890</td><td>1234567890</td><td>1234567890</td></tr>
        <tr><td>Text here</td><td>1234567890</td><td>1234567890</td><td>1234567890</td><td>1234567890</td></tr>
        <tr><td>Text here</td><td>1234567890</td><td>1234567890</td><td>1234567890</td><td>1234567890</td></tr>
        <tr><td>Text here</td><td>1234567890</td><td>1234567890</td><td>1234567890</td><td>1234567890</td></tr>
        <tr><td>Text here</td><td>1234567890</td><td>1234567890</td><td>1234567890</td><td>1234567890</td></tr>
        <tr><td>Text here</td><td>1234567890</td><td>1234567890</td><td>1234567890</td><td>1234567890</td></tr>
        <tr><td>Text here</td><td>1234567890</td><td>1234567890</td><td>1234567890</td><td>1234567890</td></tr>
      </tbody>
    </table>
    <div class="brand brand--small">Quenderix</div>
  </section>

  <section class="slide s-thanks">
    <div class="cover-photo" role="img" aria-label="Photo collage of coins, stacked receipt paper rolls and a warehouse"></div>
    <div class="cover-brand brand brand--large">Quenderix</div>
    <h1 class="cover-heading">Thank You</h1>
    <p class="cover-date">November 15, 2013</p>
  </section>

</main>
</body>
</html>
```